Business Card Design Competition

We need a business card design for our Internet Marketing company. We require both front and back designs and the final card must be 89x53mm in size, plus crop marks to 91x55mm. Colours as per logo, plus perhaps black and/or grey (#828282).
Final text must be editable (if you can supply an editable Fireworks PNG, even better)...
FRONT TEXT:
Full Name
Position
Address Line
Suburb, State, Postcode
Phone: 0000 000 000
Mobile: 0000 000 000
Email: xxx@brimleafpromo.com.au
Web: www.brimleafpromo.com.au
Rear of card should be a fresh design plus our slogan text: "Getting You Noticed" in large font, then in small text "Brimleaf Holdings Pty Ltd (ABN: 42 563 701 384)".
Target Market(s)
Small/Medium Businesses
Industry/Entity Type
Business
Look and feel
Each slider illustrates characteristics of the customer's brand and the style your logo design should communicate.

```html
<!DOCTYPE html>
<html lang="en">
<head>
<meta charset="utf-8">
<title>Brimleaf Promo – Business Card</title>
<link rel="stylesheet" href="https://fonts.googleapis.com/css2?family=Arimo:wght@400;700&display=swap">
<style>
  :root {
    --page: #ffffff;
    --card: #555555;
    --card-edge: #9a9a9a;
    --band: #c9e2a6;
    --brand-light: #dcefc2;
    --ring: #e6e6e6;
    --contact: #f5a524;
  }
  html, body {
    margin: 0;
    padding: 0;
    width: 970px;
    height: 1200px;
    overflow: hidden;
    background: var(--page);
    font-family: "Arimo", Arial, sans-serif;
  }
  .canvas {
    position: relative;
    width: 970px;
    height: 1200px;
  }
  .card {
    position: absolute;
    left: 11px;
    width: 947px;
    background: var(--card);
    border: 2px solid var(--card-edge);
    border-radius: 34px;
    overflow: hidden;
    box-sizing: border-box;
  }
  .card--front { top: 11px; height: 571px; }
  .card--back  { top: 609px; height: 578px; }
  .card__band {
    position: absolute;
    left: 0;
    right: 0;
    bottom: 0;
    height: 50px;
    background: var(--band);
  }
  .brand-mark {
    position: absolute;
    left: 24px;
    top: 108px;
    width: 330px;
    height: 330px;
  }
  .brand-name {
    position: absolute;
    left: 360px;
    top: 175px;
    margin: 0;
    color: var(--brand-light);
    font-weight: 400;
    line-height: 1;
  }
  .brand-name__first {
    display: block;
    font-size: 118px;
    letter-spacing: 3px;
  }
  .brand-name__second {
    display: block;
    margin-top: 8px;
    margin-left: 40px;
    font-size: 84px;
    letter-spacing: 4px;
  }
  .back-decoration {
    position: absolute;
    left: 440px;
    top: 10px;
    width: 560px;
    height: 560px;
  }
  .contact {
    position: relative;
    z-index: 1;
    position: absolute;
    left: 86px;
    top: 86px;
    margin: 0;
    color: var(--contact);
    font-size: 29px;
    line-height: 32px;
    font-style: normal;
  }
  .contact__group { margin: 0 0 50px; }
  .contact__group:last-child { margin-bottom: 0; }
  .contact__line { display: block; }
</style>
</head>
<body>
<main class="canvas">
  <section class="card card--front" aria-label="Card front">
    <svg class="brand-mark" viewBox="0 0 330 330" aria-hidden="true">
      <circle cx="165" cy="165" r="150" fill="none" stroke="var(--brand-light)" stroke-width="14"/>
    </svg>
    <h1 class="brand-name">
      <span class="brand-name__first">Brimleaf</span>
      <span class="brand-name__second">Promo</span>
    </h1>
    <div class="card__band"></div>
  </section>

  <section class="card card--back" aria-label="Card back">
    <svg class="back-decoration" viewBox="0 0 560 560" aria-hidden="true">
      <circle cx="280" cy="280" r="250" fill="none" stroke="var(--ring)" stroke-width="40"/>
    </svg>
    <address class="contact">
      <p class="contact__group">
        <span class="contact__line">Full Name</span>
        <span class="contact__line">Position</span>
      </p>
      <p class="contact__group">
        <span class="contact__line">Address Line</span>
        <span class="contact__line">Suburb, State, Postcode</span>
      </p>
      <p class="contact__group">
        <span class="contact__line">Phone: 0000 000 000</span>
        <span class="contact__line">Mobile: 0000 000 000</span>
      </p>
      <p class="contact__group">
        <span class="contact__line">Email: xxx@brimleafpromo.com.au</span>
        <span class="contact__line">Web: www.brimleafpromo.com.au</span>
      </p>
    </address>
    <div class="card__band"></div>
  </section>
</main>
</body>
</html>
```